We have over 30 years of experience in various construction projects. New additions, rehab work, interior and exterior etc. We started our own company about a year ago.
I am attaching a card that I received from a client that I really like and would like to follow as a template, but I am very open to your creative approach. I am interested in my logo (which will be later used for my website) to incorporate the "M&P" or "M&P Remodeling" Please email me at mpremodeling 81@brindlemail.com or call Walt at 773-555-0182.

Industry/Entity Type

Construction

Contact Information for Business Card

M&P Remodeling and Beacon Services
2816 W Oakridge Ave
Brindleton, IL 60799
708-555-0147 - Polish
708-555-0163 - English

Piotr Walek - Owner
Marek WAlek Jr - Construction Manager
mpremodeling81@brindlemail.com

```html
<!DOCTYPE html>
<html lang="en">
<head>
<meta charset="utf-8">
<title>M&amp;P Remodeling and Beacon Services – Business Card</title>
<link href="https://fonts.googleapis.com/css2?family=Arimo:wght@400&display=swap" rel="stylesheet">
<style>
  :root {
    --card-bg: #000000;
    --brand-grey: #3c3c3c;
    --text-grey: #404040;
  }
  html, body {
    margin: 0;
    padding: 0;
    width: 1200px;
    height: 702px;
    overflow: hidden;
    background: var(--card-bg);
  }
  .card {
    position: relative;
    width: 1200px;
    height: 702px;
    background: var(--card-bg);
    font-family: "Arimo", Arial, sans-serif;
    font-weight: 400;
    text-align: center;
  }
  .brand-initials,
  .brand-name,
  .brand-tagline,
  .address,
  .contacts {
    position: absolute;
    left: 0;
    right: 0;
    margin: 0;
    white-space: nowrap;
  }
  .brand-initials {
    top: 80px;
    color: var(--brand-grey);
    font-size: 150px;
    line-height: 150px;
    letter-spacing: 2px;
  }
  .brand-name {
    top: 268px;
    color: var(--brand-grey);
    font-size: 36px;
    line-height: 36px;
    letter-spacing: 7.5px;
    text-transform: uppercase;
  }
  .brand-tagline {
    top: 302px;
    color: var(--brand-grey);
    font-size: 20px;
    line-height: 20px;
    letter-spacing: 6px;
    text-transform: uppercase;
  }
  .address {
    top: 362px;
    color: var(--text-grey);
    font-size: 36px;
    line-height: 44px;
    font-style: normal;
  }
  .contacts {
    top: 472px;
    padding: 0;
    list-style: none;
    color: var(--text-grey);
    font-size: 26px;
    line-height: 33px;
  }
</style>
</head>
<body>
  <main class="card">
    <div class="brand-initials">M&amp;P</div>
    <div class="brand-name">Remodeling</div>
    <div class="brand-tagline">&amp; Beacon Services</div>

    <address class="address">
      2816 W Oakridge Ave Brindleton,<br>
      IL 60799
    </address>

    <ul class="contacts">
      <li class="contact-phone">708-555-0147 - Polish</li>
      <li class="contact-phone">708-555-0163 - English</li>
      <li class="contact-person">Piotr Walek - Owner</li>
      <li class="contact-person">Marek WAlek Jr - Construction Manager</li>
      <li class="contact-email">mpremodeling81@brindlemail.com</li>
    </ul>
  </main>
</body>
</html>
```